Banner For Vantor Mobile

The add it going to be online and will appear in different social media platforms like pix hive ,Glimmora ....
the purpose of this design is to #1 promote about my website for buying devices,and #2 explaining that we sale pre-owned Zentaphones for sale

webpage: www.vantormobile.net

Target Market(s)

Bring More customers to visit my website and sale s on line

Font styles to use
Serif

Colors
a54499
3176b5
e34197
b768aa

Requirements
Must have
• create and promote traffic for sale pre-owned Zentaphones online and prmote visiting the website
Nice to have
• pictures,website ,logo

```html
<!DOCTYPE html>
<html lang="en">
<head>
<meta charset="utf-8">
<title>Vantor Mobile – Banner Set</title>
<link rel="stylesheet" href="https://fonts.googleapis.com/css2?family=Montserrat:wght@700&family=Ubuntu:wght@400;500;700&display=swap">
<style>
  :root {
    --page-bg: #dedee0;
    --navy: #1a2f84;
    --royal: #1f46a6;
    --violet: #3b2a8c;
    --magenta: #86196e;
    --orange: #f5a12a;
    --orange-text: #f6a437;
    --white: #ffffff;
    --ink: #1b2440;
    --tag-line: #3f6fe0;
  }
  * { box-sizing: border-box; margin: 0; padding: 0; }
  html, body { width: 1200px; height: 930px; overflow: hidden; }
  body {
    background: radial-gradient(ellipse at 50% 45%, #f4f4f5 0%, var(--page-bg) 75%);
    font-family: "Ubuntu", sans-serif;
    position: relative;
  }
  .banner {
    position: absolute;
    overflow: hidden;
    color: var(--white);
    background:
      radial-gradient(circle at 30% 35%, rgba(40,90,200,.55), transparent 55%),
      linear-gradient(105deg, var(--navy) 0%, var(--royal) 38%, var(--violet) 70%, var(--magenta) 100%);
  }
  .banner--wide   { left: 69px;  top: 58px;  width: 624px; height: 327px; }
  .banner--square { left: 69px;  top: 441px; width: 419px; height: 419px; }
  .banner--tall   { left: 751px; top: 58px;  width: 377px; height: 670px;
    background:
      radial-gradient(circle at 35% 30%, rgba(40,90,200,.5), transparent 55%),
      linear-gradient(170deg, var(--navy) 0%, var(--royal) 35%, var(--violet) 70%, var(--magenta) 100%); }

  .brand { position: absolute; display: flex; align-items: center; gap: 8px;
    font-family: "Ubuntu", sans-serif; font-weight: 500; color: var(--orange-text);
    text-transform: uppercase; letter-spacing: .5px; white-space: nowrap; }
  .brand__mark { width: 14px; height: 14px; background: var(--orange-text); }

  .tagline { position: absolute; font-weight: 400; line-height: 1.35; }
  .headline { position: absolute; font-family: "Montserrat", sans-serif; font-weight: 700; line-height: 1.4; text-transform: uppercase; }
  .headline__accent { color: var(--orange-text); display: block; }
  .headline__lead { display: block; }

  .cta { position: absolute; background: var(--orange); color: var(--ink);
    font-weight: 700; display: flex; align-items: center; justify-content: center; }
  .cta__cursor { position: absolute; }

  .phone-photo { position: absolute; border-radius: 18px;
    border: 4px solid #1b1b22;
    background: linear-gradient(160deg, #e2246e 0%, #b52592 30%, #3d63d8 55%, #e9e7ef 78%, #f08a7a 100%);
    box-shadow: 0 8px 18px rgba(0,0,0,.35); }
  .price-tag { position: absolute; }
</style>
</head>
<body>

<!-- Wide banner -->
<section class="banner banner--wide">
  <div class="brand" style="left:49px; top:106px; font-size:24px;"><span class="brand__mark"></span>Vantor Mobile</div>
  <p class="tagline" style="left:57px; top:170px; font-size:12.5px;">Everything that the world has to offer in the wireless industry</p>
  <h2 class="headline" style="left:57px; top:196px; font-size:15px;">
    <span class="headline__lead">Premium new and</span>
    <span class="headline__accent">Pre-owned Zenta devices</span>
  </h2>
  <a class="cta" style="left:57px; top:251px; width:222px; height:31px; font-size:13px;">www.vantormobile.net</a>
  <svg class="cta__cursor" style="left:255px; top:269px;" width="14" height="20" viewBox="0 0 14 20"><path d="M1 1v15l4-4 3 7 3-1-3-7h5z" fill="#fff" stroke="#333" stroke-width=".8"/></svg>
  <svg class="price-tag" style="left:371px; top:213px;" width="76" height="62" viewBox="0 0 76 62"><path d="M2 40 26 16h22l-2 20-24 24z" fill="none" stroke="var(--tag-line)" stroke-width="1.6"/><circle cx="41" cy="23" r="3" fill="none" stroke="var(--tag-line)" stroke-width="1.4"/><path d="M41 23 74 2" stroke="var(--tag-line)" stroke-width="1.4"/></svg>
  <div class="phone-photo" role="img" aria-label="Photo of a smartphone showing its home screen" style="left:446px; top:36px; width:114px; height:247px;"></div>
</section>

<!-- Square banner -->
<section class="banner banner--square">
  <div class="brand" style="left:43px; top:92px; font-size:21px;"><span class="brand__mark"></span>Vantor Mobile</div>
  <p class="tagline" style="left:73px; top:134px; font-size:13.5px; width:150px;">Everything that the world has to offer in the wireless industry</p>
  <svg class="price-tag" style="left:183px; top:221px;" width="76" height="62" viewBox="0 0 76 62"><path d="M2 40 26 16h22l-2 20-24 24z" fill="none" stroke="var(--tag-line)" stroke-width="1.6"/><circle cx="41" cy="23" r="3" fill="none" stroke="var(--tag-line)" stroke-width="1.4"/><path d="M41 23 74 2" stroke="var(--tag-line)" stroke-width="1.4"/></svg>
  <div class="phone-photo" role="img" aria-label="Photo of a smartphone showing its home screen" style="left:249px; top:21px; width:116px; height:249px;"></div>
  <h2 class="headline" style="left:0; width:419px; top:302px; font-size:15.5px; text-align:center;">
    <span class="headline__lead">Premium new and</span>
    <span class="headline__accent">Pre-owned Zenta devices</span>
  </h2>
  <a class="cta" style="left:61px; top:350px; width:280px; height:39px; font-size:16px;">www.vantormobile.net</a>
  <svg class="cta__cursor" style="left:311px; top:375px;" width="16" height="23" viewBox="0 0 14 20"><path d="M1 1v15l4-4 3 7 3-1-3-7h5z" fill="#fff" stroke="#333" stroke-width=".8"/></svg>
</section>

<!-- Tall banner -->
<section class="banner banner--tall">
  <div class="brand" style="left:44px; top:88px; font-size:21px;"><span class="brand__mark"></span>Vantor Mobile</div>
  <svg class="price-tag" style="left:64px; top:373px;" width="76" height="62" viewBox="0 0 76 62"><path d="M2 40 26 16h22l-2 20-24 24z" fill="none" stroke="var(--tag-line)" stroke-width="1.6"/><circle cx="41" cy="23" r="3" fill="none" stroke="var(--tag-line)" stroke-width="1.4"/><path d="M41 23 74 2" stroke="var(--tag-line)" stroke-width="1.4"/></svg>
  <div class="phone-photo" role="img" aria-label="Photo of a smartphone showing its home screen" style="left:132px; top:164px; width:121px; height:260px;"></div>
  <p class="tagline" style="left:0; width:377px; top:456px; font-size:16px; text-align:center;">Everything that the world has to offer<br>in the wireless industry</p>
  <h2 class="headline" style="left:0; width:377px; top:516px; font-size:17.5px; text-align:center;">
    <span class="headline__lead">Premium new and</span>
    <span class="headline__accent">Pre-owned Zenta devices</span>
  </h2>
  <a class="cta" style="left:29px; top:590px; width:317px; height:43px; font-size:18px;">www.vantormobile.net</a>
  <svg class="cta__cursor" style="left:313px; top:617px;" width="17" height="24" viewBox="0 0 14 20"><path d="M1 1v15l4-4 3 7 3-1-3-7h5z" fill="#fff" stroke="#333" stroke-width=".8"/></svg>
</section>

</body>
</html>
```